Create Print and Packaging Designs for Vellara Beauty - Tweezers Box

I am in the process of releasing a new Product to be sold on [url removed, login to view] - A Set of tweezers - The Difference between this product an others is it will be packaged in a Clean Plastic Box, with a Printed Paper Liner - The supplier can give me a blank Layout in Photoshop Illustrator Format

The Box Size is - :50x25x180mm

I have used this type of Box before - Here is how it came out - (Final Product will be shown in a similar way) - [url removed, login to view]

What I need is Design for the Box for Printing - I have a logo already here - [url removed, login to view] (logo I like - Text- not so much)

The outcome I am looking for is something similar to this: [url removed, login to view]

This is a 3D Render- And I will also be doing similar output

The purpose is ensure my product looks fantastic when viewed beside similar choices on Quorbin - so please make yourself familiar with results at quorbin for the search term tweezer

I have added another Example image of the finger nail clippers - Not the Printer Area is paper and sits underneath the item, the side of the box and curved section on the top.

I have also included the PDF outline

I am looking for someone with a creative Eye which can take the ideas to another level - I am looking for long term Business relationship and fast and clear communication. Meeting of time frames and expectations will be key. In short a Graphics professional who is also a business professional.

Edit; Not that a lot of the Current designs have decorated the "Underside" of the box - an it wont be seen. There are than can be designed on the Inside of the box- around the tweezer - See the green picture example

Actual product image added - please use in samples

```html
<!DOCTYPE html>
<html lang="en">
<head>
<meta charset="utf-8">
<title>Vellara Beauty – Tweezer Set Packaging</title>
<link rel="stylesheet" href="https://fonts.googleapis.com/css2?family=Lobster&family=Dancing+Script:wght@600&display=swap">
<style>
  :root {
    --backdrop: #d9d9db;
    --liner-peach: #f8d7bd;
    --liner-light: #fbe6d4;
    --plum: #a2327f;
    --orchid: #c35aa8;
    --magenta: #d4147a;
    --sun: #ffe14a;
    --ink: #231a1f;
    --steel-light: #eef0f2;
    --steel-dark: #a9adb3;
  }
  html, body {
    margin: 0;
    width: 1152px;
    height: 1200px;
    overflow: hidden;
    background: var(--backdrop);
  }
  .package {
    position: absolute;
    left: 186px;
    top: 60px;
    width: 780px;
    height: 1080px;
    display: flex;
  }
  .side-panel {
    position: relative;
    width: 150px;
    margin-top: 380px;
    height: 700px;
    background: var(--liner-peach);
    overflow: hidden;
  }
  .side-panel__band {
    position: absolute;
    left: 0; top: 0;
    width: 150px;
    height: 150px;
  }
  .side-panel__slogan {
    position: absolute;
    left: 75px;
    top: 400px;
    transform: translate(-50%, -50%) rotate(90deg);
    white-space: nowrap;
    font-family: "Lobster", cursive;
    font-size: 46px;
    color: var(--magenta);
    -webkit-text-stroke: 1px var(--sun);
  }
  .front-panel {
    position: relative;
    width: 630px;
    height: 1080px;
    background: var(--liner-light);
  }
  .header-card {
    position: absolute;
    left: 0; top: 0;
    width: 630px;
    height: 380px;
    background: var(--liner-peach);
    display: flex;
    flex-direction: column;
    align-items: center;
  }
  .brand-mark {
    margin-top: 70px;
    display: flex;
    align-items: center;
    gap: 16px;
  }
  .brand-mark__dot {
    width: 64px;
    height: 64px;
    border-radius: 50%;
    background: var(--orchid);
  }
  .brand-mark__name {
    font-family: "Dancing Script", cursive;
    font-weight: 600;
    font-size: 40px;
    color: var(--plum);
  }
  .brand-name {
    margin-top: 60px;
    font-family: "Dancing Script", cursive;
    font-weight: 600;
    font-size: 70px;
    color: var(--ink);
  }
  .title-arch {
    position: absolute;
    left: 0; top: 380px;
    width: 630px;
    height: 200px;
  }
  .title-arch__main {
    position: absolute;
    left: 0; right: 0; top: 22px;
    text-align: center;
    font-family: "Lobster", cursive;
    font-size: 74px;
    color: var(--magenta);
    -webkit-text-stroke: 2px var(--sun);
    paint-order: stroke fill;
  }
  .title-arch__sub {
    position: absolute;
    left: 0; right: 0; top: 118px;
    text-align: center;
    font-family: "Lobster", cursive;
    font-size: 40px;
    color: var(--magenta);
  }
  .product-window {
    position: absolute;
    left: 30px;
    top: 580px;
    width: 570px;
    height: 470px;
    border-radius: 6px;
    background: linear-gradient(90deg, var(--steel-dark), var(--steel-light) 20%, var(--steel-dark) 40%, var(--steel-light) 60%, var(--steel-dark) 80%, var(--steel-light));
  }
</style>
</head>
<body>
  <div class="package">
    <div class="side-panel">
      <svg class="side-panel__band" viewBox="0 0 150 150" aria-hidden="true">
        <path d="M0 0 H150 V70 Q75 150 0 110 Z" fill="var(--orchid)"/>
      </svg>
      <div class="side-panel__slogan">Beauty can be FUN!</div>
    </div>
    <div class="front-panel">
      <header class="header-card">
        <div class="brand-mark">
          <span class="brand-mark__dot"></span>
          <span class="brand-mark__name">Vellara Beauty</span>
        </div>
        <div class="brand-name">Vellara Beauty</div>
      </header>
      <div class="title-arch">
        <svg width="630" height="200" viewBox="0 0 630 200" aria-hidden="true">
          <path d="M0 40 Q315 -10 630 40 V190 Q315 150 0 190 Z" fill="var(--liner-peach)"/>
        </svg>
        <div class="title-arch__main">Tweezer Set</div>
        <div class="title-arch__sub">Precision Grooming Kit</div>
      </div>
      <div class="product-window" role="img" aria-label="Photo of six stainless steel tweezers standing side by side"></div>
    </div>
  </div>
</body>
</html>
```